Poster for List of Company Values

We need a poster to outline our Values which will be displayed in our office as well as posted on our website and other platforms (so need to allow for some flexibly in its application).

File attached outlines what we currently have with design and also our company style guide.

Note that we are looking for a modern, clean look, which still represents our core activities of construction and environmental services.

You can also reference our website here:

https://quorvelgroup.com.au/

Happy to answer any questions you might have.

Thanks for your interest,
Brent

Target Market(s)

Internal and External clients

Industry/Entity Type

Construction, water and recycling

Font styles to use
Sans Serif

Requirements
Must have
• All values on the one page. Graphic to represent each value. Also needs to use company logo
Nice to have
• Preference for poster to be orientated in landscape
Should not have
• Do not follow example provided, this is only to demonstrate what we have to date and also the text required

```html
<!DOCTYPE html>
<html lang="en">
<head>
<meta charset="utf-8">
<title>Quorvel Group — Our Values</title>
<link rel="stylesheet" href="https://fonts.googleapis.com/css2?family=Poppins:wght@400;500;600;700;800&display=swap">
<style>
  :root {
    --page-bg: #f3f3f5;
    --loyal-green: #4eab4a;
    --initiative-yellow: #fcc212;
    --team-blue: #1172bb;
    --respect-orange: #ee7d31;
    --honest-pink: #ee3190;
    --positive-cyan: #28aee4;
    --ink-light: #ffffff;
  }
  * { box-sizing: border-box; margin: 0; padding: 0; }
  html, body {
    width: 1200px; height: 1000px; overflow: hidden;
    background: var(--page-bg);
    font-family: "Poppins", sans-serif;
    color: var(--ink-light);
  }
  .values-board { position: relative; width: 1200px; height: 1000px; }
  .value-tile {
    position: absolute; width: 357px; height: 356px; overflow: hidden;
  }
  .tile-loyal { left: 53px; top: 126px; background: var(--loyal-green); }
  .tile-initiative { left: 422px; top: 126px; background: var(--initiative-yellow); }
  .tile-team { left: 790px; top: 126px; background: var(--team-blue); }
  .tile-respect { left: 53px; top: 494px; background: var(--respect-orange); }
  .tile-honest { left: 422px; top: 494px; background: var(--honest-pink); }
  .tile-positive { left: 790px; top: 494px; background: var(--positive-cyan); }

  .brand-mark {
    position: absolute; left: 18px; top: 18px;
    display: flex; align-items: center; gap: 6px;
  }
  .brand-square { width: 18px; height: 18px; background: var(--ink-light); }
  .brand-name {
    font-weight: 500; font-size: 10.5px; line-height: 11px; color: var(--ink-light);
  }

  .value-text {
    position: absolute; font-weight: 600; font-size: 14px; line-height: 21px;
    white-space: nowrap;
  }
  .value-title { position: absolute; line-height: 1; white-space: nowrap; }
  .title-light { font-weight: 400; }
  .title-bold { font-weight: 800; letter-spacing: -1px; }

  /* Be Loyal */
  .tile-loyal .value-text { left: 19px; top: 100px; }
  .tile-loyal .title-line-1 { left: 17px; top: 191px; font-size: 80px; }
  .tile-loyal .title-line-2 { left: 16px; top: 270px; font-size: 80px; }

  /* Show Initiative */
  .tile-initiative .vertical-title {
    position: absolute; right: 18px; top: 47px;
    writing-mode: vertical-rl; font-size: 53px; line-height: 49px; white-space: nowrap;
  }
  .tile-initiative .value-text { left: 18px; top: 254px; }

  /* Think Team */
  .tile-team .title-line-1 { left: 48px; top: 80px; font-size: 80px; }
  .tile-team .title-line-2 { left: 44px; top: 159px; font-size: 80px; }
  .tile-team .value-text {
    left: 51px; top: 240px; width: 254px; white-space: normal;
    text-align: justify; text-align-last: center;
  }

  /* Show Respect */
  .tile-respect .value-text { left: 18px; top: 114px; }
  .tile-respect .title-line-1 { right: 17px; top: 217px; font-size: 68px; }
  .tile-respect .title-line-2 { right: 18px; top: 280px; font-size: 68px; }

  /* Be Open & Honest */
  .tile-honest .title-line-1 { left: 18px; top: 100px; font-size: 57px; }
  .tile-honest .title-line-2 { left: 17px; top: 156px; font-size: 57px; }
  .tile-honest .value-text { left: 18px; top: 220px; }

  /* Be Positive */
  .tile-positive .title-line-1 { left: 18px; top: 76px; font-size: 63px; }
  .tile-positive .title-line-2 { left: 17px; top: 137px; font-size: 63px; }
  .tile-positive .value-text { right: 17px; top: 220px; text-align: right; }
  .value-keyword { font-weight: 800; }
</style>
</head>
<body>
<main class="values-board">

  <section class="value-tile tile-loyal">
    <div class="brand-mark"><span class="brand-square"></span><span class="brand-name">QUORVEL<br>Group</span></div>
    <p class="value-text">We take care of our own and provide<br>opportunities to listen and support each<br>other.</p>
    <h2 class="value-title title-line-1 title-light">‘BE</h2>
    <h2 class="value-title title-line-2 title-bold">LOYAL’</h2>
  </section>

  <section class="value-tile tile-initiative">
    <div class="brand-mark"><span class="brand-square"></span><span class="brand-name">QUORVEL<br>Group</span></div>
    <h2 class="vertical-title"><span class="title-light">‘SHOW</span><br><span class="title-bold">INITIATIVE’</span></h2>
    <p class="value-text">We celebrate and<br>recognize our own and<br>encourage forward<br>thinking.</p>
  </section>

  <section class="value-tile tile-team">
    <div class="brand-mark"><span class="brand-square"></span><span class="brand-name">QUORVEL<br>Group</span></div>
    <h2 class="value-title title-line-1 title-light">‘THINK</h2>
    <h2 class="value-title title-line-2 title-bold">TEAM’</h2>
    <p class="value-text">We communicate effectively and work as a team by helping and supporting each other.</p>
  </section>

  <section class="value-tile tile-respect">
    <div class="brand-mark"><span class="brand-square"></span><span class="brand-name">QUORVEL<br>Group</span></div>
    <p class="value-text">We value the diversity and<br>opinions of all.</p>
    <h2 class="value-title title-line-1 title-light">‘SHOW</h2>
    <h2 class="value-title title-line-2 title-bold">RESPECT’</h2>
  </section>

  <section class="value-tile tile-honest">
    <div class="brand-mark"><span class="brand-square"></span><span class="brand-name">QUORVEL<br>Group</span></div>
    <h2 class="value-title title-line-1"><span class="title-light">‘BE </span><span class="title-bold">OPEN</span><span class="title-light"> &amp;</span></h2>
    <h2 class="value-title title-line-2 title-bold">HONEST’</h2>
    <p class="value-text">We are clear and open with each other,<br>and provide an approachable and<br>friendly environment.</p>
  </section>

  <section class="value-tile tile-positive">
    <div class="brand-mark"><span class="brand-square"></span><span class="brand-name">QUORVEL<br>Group</span></div>
    <h2 class="value-title title-line-1 title-light">‘BE</h2>
    <h2 class="value-title title-line-2 title-bold">POSITIVE’</h2>
    <p class="value-text"><span class="value-keyword">SMILE</span><br>We are solutions focused and<br>encourage a positive attitude turning a<br>negative into a positive.</p>
  </section>

</main>
</body>
</html>
```